Kickass billboard for motorway

Fix my old hauler - clue is in the name.
We have a 45ft billboard we're looking to design constructed from an old trailer we own (so we can be as creative as possible).
We provide a van buying service, being one of the only companies in the UK with the facilities to recover faulty, damaged and broken vans - from small car derived vans to large trucks and lorries.
ur niche in the market is different to car buying services, as buying and selling cars is often an emotionally driven process, whereas people often see and treat vans purely as a tool. There are alternatives to a car, public transport etc, but not to a work van - so people go out straight away and replace them immediately, often leaving the old broken van to sit on their drive or in their unit.
Looking to start building a brand asset bank.
Feel free to check out our website to get a feel for what we do:
Fixmyoldhauler.co.uk

Target Market(s)

Van owners/drivers & fleet managers

Industry/Entity Type

Automotive

Font styles to use
Sans Serif

Colors
34a7d8

Requirements
Must have
• Eye-catching - very eye-catching.
We want to advertise the fact we collect vehicles for free.
We pay instantly upon arrival.
Our phone number 0161 493 7062
Our website www.fixmyoldhauler.co.uk
Nice to have
• 3d elements - we have the ability to get 3d props for the billboard including damaged vans etc.

```html
<!DOCTYPE html>
<html lang="en">
<head>
<meta charset="utf-8">
<title>Sell Your Van – Fix my old hauler billboard</title>
<link rel="stylesheet" href="https://fonts.googleapis.com/css2?family=Arimo:wght@400;700&display=swap">
<style>
  :root {
    --brand-blue: #34a7d8;
    --brand-blue-light: #6cc4e8;
    --ink-navy: #1c2a37;
    --footer-navy: #1f2c38;
    --paper: #ffffff;
    --backdrop: #e8edf1;
    --van-teal: #7fc9c4;
    --van-teal-dark: #3e8e8c;
  }
  * { box-sizing: border-box; margin: 0; padding: 0; }
  html, body {
    width: 876px;
    height: 1200px;
    overflow: hidden;
    background: var(--backdrop);
    font-family: "Arimo", Arial, sans-serif;
  }
  .billboard {
    position: absolute;
    left: 20px;
    top: 350px;
    width: 836px;
    height: 500px;
    background: var(--paper);
    box-shadow: 0 6px 24px rgba(0,0,0,0.15);
    overflow: hidden;
  }
  .headline-band {
    position: absolute;
    left: 0; top: 0;
    width: 100%;
    height: 96px;
    background: var(--brand-blue);
    border-bottom: 6px solid var(--brand-blue-light);
    display: flex;
    align-items: center;
    justify-content: center;
  }
  .headline {
    font-weight: 700;
    font-size: 66px;
    letter-spacing: 1px;
    color: var(--ink-navy);
    white-space: nowrap;
  }
  .offer {
    position: absolute;
    left: 32px;
    top: 150px;
    width: 400px;
    color: var(--ink-navy);
  }
  .offer-line { display: block; white-space: nowrap; }
  .offer-collect {
    font-weight: 700;
    font-size: 23px;
    line-height: 1.22;
  }
  .offer-pay {
    margin-top: 30px;
    font-weight: 700;
    font-size: 37px;
    line-height: 1.12;
  }
  .van-prop {
    position: absolute;
    left: 444px;
    top: 116px;
    width: 372px;
    height: 286px;
    border-radius: 40px 60px 18px 18px;
    background: radial-gradient(ellipse at 55% 45%, var(--van-teal) 0%, var(--van-teal-dark) 75%, #d9e4e6 100%);
  }
  .contact-bar {
    position: absolute;
    left: 0; bottom: 0;
    width: 100%;
    height: 82px;
    background: var(--footer-navy);
    display: flex;
    align-items: center;
    color: var(--paper);
    white-space: nowrap;
  }
  .call-now {
    margin-left: 22px;
    font-weight: 700;
    font-size: 20px;
    line-height: 1.05;
  }
  .phone {
    font-weight: 700;
    font-size: 42px;
    letter-spacing: 0.5px;
    margin-left: 14px;
  }
  .divider {
    flex: none;
    width: 3px;
    height: 60px;
    background: var(--paper);
    margin: 0 18px;
  }
  .website {
    font-weight: 700;
    font-size: 19px;
    color: var(--brand-blue-light);
    text-transform: uppercase;
  }
</style>
</head>
<body>
  <main class="billboard">
    <header class="headline-band">
      <h1 class="headline">SELL YOUR VAN</h1>
    </header>

    <section class="offer">
      <p class="offer-collect">
        <span class="offer-line">We want to advertise the fact</span>
        <span class="offer-line">we collect vehicles for free.</span>
      </p>
      <p class="offer-pay">
        <span class="offer-line">WE PAY INSTANTLY</span>
        <span class="offer-line">UPON ARRIVAL.</span>
      </p>
    </section>

    <div class="van-prop" role="img" aria-label="Photo of a damaged teal van with a crumpled front end"></div>

    <footer class="contact-bar">
      <p class="call-now">CALL<br>NOW!</p>
      <p class="phone">0161 493 7062</p>
      <span class="divider"></span>
      <p class="website">www.fixmyoldhauler.co.uk</p>
    </footer>
  </main>
</body>
</html>
```